Zielgruppe
Steuerberatung
Aufgabenstellung
Ich benötige eine Neuerstellung für ein vorhandenes Briefpapier. Bedeutet, eigentlich soll der aktuelle Inhalt neu erstellt werden, da mir die Rohdaten nicht mehr zur Verfügung stehen. Das aktuelle Briefpapier steht als .doc zur Verfügung. Ziel 1:1 Abbildung. Zudem muss die Adresse geändert werden.

```html
<!DOCTYPE html>
<html lang="de">
<head>
<meta charset="utf-8">
<title>Briefpapier Steuerberatung Brenneke</title>
<link href="https://fonts.googleapis.com/css2?family=Roboto+Condensed:wght@400;700&display=swap" rel="stylesheet">
<style>
  :root {
    --backdrop: #e9cdb6;
    --paper: #ffffff;
    --ink: #1c1c1c;
    --mark-tint: #e6e6e6;
    --rule: #222222;
  }
  html, body {
    margin: 0;
    padding: 0;
    width: 1200px;
    height: 1200px;
    overflow: hidden;
    background: var(--backdrop);
    font-family: "Roboto Condensed", "Arial Narrow", sans-serif;
    color: var(--ink);
  }
  .stationery {
    position: relative;
    width: 1200px;
    height: 1200px;
  }
  .sheet {
    position: absolute;
    top: 216px;
    width: 542px;
    height: 766px;
    background: var(--paper);
    overflow: hidden;
    box-shadow: 0 6px 18px rgba(90, 60, 40, 0.25);
  }
  .sheet--first { left: 22px; }
  .sheet--follow { left: 636px; }

  .brand-mark {
    position: absolute;
    right: 130px;
    top: 86px;
    width: 220px;
    height: 220px;
    right: -40px;
    top: auto;
    bottom: -30px;
    background: var(--mark-tint);
  }

  .sender-line {
    position: absolute;
    left: 52px;
    top: 115px;
    font-size: 5.4px;
    letter-spacing: 0.05px;
    white-space: nowrap;
  }
  .sender-line .sep, .footer .sep, .contact-name .sep { padding: 0 3px; }

  .brand-name {
    position: absolute;
    left: 394px;
    top: 70px;
    display: flex;
    align-items: center;
    gap: 6px;
    font-size: 13px;
    font-weight: 700;
    letter-spacing: 0.2px;
  }
  .brand-name .square {
    width: 12px;
    height: 12px;
    background: var(--ink);
  }

  .contact {
    position: absolute;
    left: 394px;
    top: 114px;
    font-size: 7.2px;
    line-height: 11px;
  }
  .contact-name b { font-weight: 700; }
  .contact-row { display: flex; }
  .contact-row .label { width: 20px; }

  .fold-mark {
    position: absolute;
    left: 13px;
    width: 12px;
    height: 0;
    border-top: 0.8px solid var(--rule);
  }
  .fold-mark--upper { top: 235px; }
  .fold-mark--lower { top: 505px; }

  .footer {
    position: absolute;
    left: 52px;
    top: 709px;
    font-size: 6.6px;
    line-height: 11px;
    white-space: nowrap;
  }
  .footer b { font-weight: 700; }
</style>
</head>
<body>
<main class="stationery">

  <section class="sheet sheet--first" aria-label="Briefbogen Erstseite">
    <div class="brand-mark" aria-hidden="true"></div>

    <div class="brand-name"><span class="square"></span>Brenneke</div>

    <p class="sender-line" style="margin:0">Jonas Brenneke<span class="sep">|</span>Lindenhofweg 18<span class="sep">|</span>31785 Halmstedt</p>

    <div class="contact">
      <div class="contact-name"><b>Jonas Brenneke</b><span class="sep">|</span>Steuerberater</div>
      <div class="contact-row"><span class="label">Tel.:</span><span>+49 (0) 170 - 55 20 318</span></div>
      <div class="contact-row"><span class="label">Fax.:</span><span>+49 (0) 5151 - 60 42 17 05</span></div>
      <div class="contact-row"><span class="label">Mail:</span><span>info@steuerberatung-brenneke.de</span></div>
      <div class="contact-row"><span class="label">Web:</span><span>www.steuerberatung-brenneke.de</span></div>
    </div>

    <div class="fold-mark fold-mark--upper"></div>
    <div class="fold-mark fold-mark--lower"></div>

    <footer class="footer">
      <div><b>Jonas Brenneke</b><span class="sep">|</span>Steuerberater</div>
      <div>Lindenhofweg 18<span class="sep">|</span>31785 Halmstedt<span class="sep">|</span>Zuständige Aufsichtsbehörde: Steuerberaterkammer Nordland -Körperschaft des öffentlichen Rechts-</div>
      <div>Zuständiges Finanzamt: Finanzamt Halmstedt-Mitte, Steuernummer: 31/207/48816<span class="sep">|</span>Bankverbindung: DE 47 2104 0088 0312 5579 16 BIC: NORVDE2H</div>
    </footer>
  </section>

  <section class="sheet sheet--follow" aria-label="Briefbogen Folgeseite">
    <div class="brand-mark" aria-hidden="true"></div>

    <p class="sender-line" style="margin:0">Jonas Brenneke<span class="sep">|</span>Lindenhofweg 18<span class="sep">|</span>31785 Halmstedt</p>

    <div class="fold-mark fold-mark--upper"></div>
    <div class="fold-mark fold-mark--lower"></div>

    <footer class="footer">
      <div><b>Jonas Brenneke</b><span class="sep">|</span>Steuerberater</div>
      <div>Lindenhofweg 18<span class="sep">|</span>31785 Halmstedt<span class="sep">|</span>Zuständige Aufsichtsbehörde: Steuerberaterkammer Nordland -Körperschaft des öffentlichen Rechts-</div>
      <div>Zuständiges Finanzamt: Finanzamt Halmstedt-Mitte, Steuernummer: 31/207/48816<span class="sep">|</span>Bankverbindung: DE 47 2104 0088 0312 5579 16 BIC: NORVDE2H</div>
    </footer>
  </section>

</main>
</body>
</html>
```